Looking to design a new sign for our church.

Looking for a new sign
4 x 8 feet dimension
We are renaming the church "Medlow Ridge Community Church"
looking for legible graphics
Would like some type of backdrop being a family tree (oak) / open to other ideas as you are led
I have included a pic of the old sign for your review
would like to incorporate our ministry logo on the lower right hand corner of the sign / see file attached

```html
<!DOCTYPE html>
<html lang="en">
<head>
<meta charset="utf-8">
<title>Medlow Ridge Community Church – Sign</title>
<link rel="stylesheet" href="https://fonts.googleapis.com/css2?family=Tinos:wght@400;700&display=swap">
<style>
  :root {
    --ink: #150a48;
    --oak: #1d5b38;
    --oak-soft: #3f7f57;
    --paper: #ffffff;
    --backdrop: #eef1f6;
    --frame-line: #2a2160;
  }
  * { box-sizing: border-box; margin: 0; padding: 0; }
  html, body {
    width: 849px;
    height: 1200px;
    overflow: hidden;
    background: var(--backdrop);
    font-family: "Tinos", "Times New Roman", serif;
    color: var(--ink);
  }
  .canvas {
    position: relative;
    width: 849px;
    height: 1200px;
  }
  .sign {
    position: absolute;
    left: 49px;
    top: 412px;
    width: 751px;
    height: 376px;
    background: var(--paper);
    box-shadow: 0 6px 18px rgba(20, 20, 60, 0.18);
  }
  .sign__frame {
    position: absolute;
    inset: 23px;
    border: 1px solid var(--frame-line);
  }
  .sign__cross {
    position: absolute;
    left: 40px;
    top: 43px;
    width: 43px;
    height: 68px;
  }
  .welcome {
    position: absolute;
    left: 117px;
    top: 44px;
    width: 521px;
    display: flex;
    align-items: center;
    gap: 10px;
  }
  .welcome__rule {
    flex: 1;
    height: 4px;
    background: var(--ink);
  }
  .welcome__text {
    font-size: 24px;
    letter-spacing: 0.5px;
    line-height: 1;
  }
  .church-name {
    position: absolute;
    left: 110px;
    top: 74px;
    width: 530px;
    text-align: center;
    font-size: 79px;
    line-height: 1;
    white-space: nowrap;
  }
  .subtitle {
    position: absolute;
    left: 113px;
    top: 165px;
    width: 520px;
    display: flex;
    align-items: center;
    justify-content: space-between;
  }
  .subtitle__bar {
    width: 87px;
    height: 13px;
    background: var(--ink);
  }
  .subtitle__text {
    font-size: 35px;
    letter-spacing: 2px;
    line-height: 1;
    white-space: nowrap;
  }
  .oak-tree {
    position: absolute;
    left: 320px;
    top: 238px;
    width: 111px;
    height: 89px;
    border-radius: 50% 50% 8px 8px / 60% 60% 8px 8px;
    background: radial-gradient(ellipse at 50% 40%, var(--oak-soft), var(--oak) 70%);
  }
  .ministry-mark {
    position: absolute;
    right: 40px;
    bottom: 44px;
    display: flex;
    align-items: center;
    gap: 5px;
    font-size: 11px;
    line-height: 1;
    white-space: nowrap;
  }
  .ministry-mark__dot {
    width: 10px;
    height: 10px;
    border-radius: 50%;
    background: var(--ink);
  }
</style>
</head>
<body>
<main class="canvas">
  <section class="sign" aria-label="Medlow Ridge Community Church sign">
    <div class="sign__frame"></div>

    <svg class="sign__cross" viewBox="0 0 43 68" aria-hidden="true">
      <path d="M16 1h11v16h15v11H27v39H16V28H1V17h15z" fill="none" stroke="var(--ink)" stroke-width="1.5"/>
      <path d="M19 4h5v16h15v5H24v39h-5V25H4v-5h15z" fill="var(--ink)"/>
    </svg>

    <div class="welcome">
      <span class="welcome__rule"></span>
      <span class="welcome__text">Welcome To</span>
      <span class="welcome__rule"></span>
    </div>

    <h1 class="church-name">Medlow Ridge</h1>

    <div class="subtitle">
      <span class="subtitle__bar"></span>
      <span class="subtitle__text">Community Church</span>
      <span class="subtitle__bar"></span>
    </div>

    <div class="oak-tree" role="img" aria-label="Green oak tree illustration, the family tree emblem"></div>

    <div class="ministry-mark">
      <span class="ministry-mark__dot"></span>
      <span class="ministry-mark__name">Ridge Ministry</span>
    </div>
  </section>
</main>
</body>
</html>
```